Business Card for boutique psychology business

Business card for boutique psychology practice in Melbourne. I want them to be relatively simply with the logo and backing colour taking up the front side. Then, text on the back, with my name; professional title (Clinical Psychologist); website - torvinpsychology.com.au; email: hello@torvinpsychology.com.au; insta: @torvin.psychology.emdr
Back should also have the words: Connect. Integrate. Evolve
Fonts used for logo are: Mikea Demo and Gotham Medium. Use something for back text that will compliment these.
Brand colours uploaded below. I'd like to see options in both olive and blush.

```html
<!DOCTYPE html>
<html lang="en">
<head>
<meta charset="utf-8">
<title>Torvin Psychology + EMDR — Business Card</title>
<link rel="stylesheet" href="https://fonts.googleapis.com/css2?family=Montserrat:wght@500;700&family=Open+Sans:wght@400&display=swap">
<style>
  :root {
    --backdrop: #e4e4e1;
    --blush: #ebcdbf;
    --blush-deep: #d8ad98;
    --blush-light: #f3ddd2;
    --olive: #3f4128;
    --olive-soft: #5a5b44;
  }
  * { margin: 0; padding: 0; box-sizing: border-box; }
  html, body { width: 1200px; height: 801px; overflow: hidden; }
  body {
    background: var(--backdrop);
    position: relative;
    font-family: "Open Sans", Arial, sans-serif;
    color: var(--olive);
  }
  .card {
    position: absolute;
    top: 235px;
    width: 540px;
    height: 330px;
    background: var(--blush);
    overflow: hidden;
    box-shadow: 0 10px 28px rgba(0,0,0,0.14);
  }
  /* Back of card: details */
  .card--back { left: 40px; }
  .card--back .band {
    position: absolute;
    left: 150px; top: 0;
    width: 40px; height: 100%;
    background: var(--olive);
  }
  .details {
    position: absolute;
    left: 230px; top: 46px;
  }
  .wordmark {
    font-family: "Montserrat", Arial, sans-serif;
    font-weight: 500;
    color: var(--olive);
    line-height: 1;
  }
  .wordmark .name { display: block; letter-spacing: 1px; }
  .wordmark .sub { display: block; }
  .card--back .wordmark .name { font-size: 54px; }
  .card--back .wordmark .sub { font-size: 19px; margin-top: 6px; }
  .practitioner {
    margin-top: 28px;
    font-family: "Montserrat", Arial, sans-serif;
    font-weight: 700;
    font-size: 18px;
    letter-spacing: 0.5px;
  }
  .role { font-size: 15px; color: var(--olive-soft); margin-top: 2px; }
  .contact-list { list-style: none; margin-top: 16px; }
  .contact-list li {
    display: flex; align-items: center; gap: 7px;
    font-size: 14.5px; color: var(--olive-soft); line-height: 1.45;
  }
  .contact-list .dot {
    width: 10px; height: 10px; background: var(--olive); flex: none;
  }
  .contact-list .dot--round { border-radius: 50%; }

  /* Front of card: mark + tagline */
  .card--front { left: 620px; }
  .pattern {
    position: absolute; inset: 0;
    background: linear-gradient(120deg, var(--blush-light) 0%, var(--blush) 45%, var(--blush-deep) 100%);
  }
  .front-content {
    position: absolute; inset: 0;
    display: flex; flex-direction: column; align-items: center; justify-content: center;
  }
  .card--front .wordmark { text-align: center; }
  .card--front .wordmark .name { font-size: 76px; }
  .card--front .wordmark .sub { font-size: 25px; margin-top: 8px; }
  .tagline {
    display: flex; align-items: center; gap: 10px;
    margin-top: 26px; font-size: 17px; color: var(--olive-soft);
  }
  .tagline .sep { width: 7px; height: 7px; border-radius: 50%; background: var(--olive); }
</style>
</head>
<body>
  <section class="card card--back">
    <div class="band"></div>
    <div class="details">
      <div class="wordmark">
        <span class="name">torvin</span>
        <span class="sub">psychology + EMDR</span>
      </div>
      <p class="practitioner">MARCUS HALE</p>
      <p class="role">Clinical Psychologist</p>
      <ul class="contact-list">
        <li><span class="dot"></span>@torvin.psychology.emdr</li>
        <li><span class="dot dot--round"></span>torvinpsychology.com.au</li>
        <li><span class="dot"></span>hello@torvinpsychology.com.au</li>
      </ul>
    </div>
  </section>

  <section class="card card--front">
    <div class="pattern" role="img" aria-label="Embossed pattern of repeating leaf shapes in blush tones"></div>
    <div class="front-content">
      <div class="wordmark">
        <span class="name">torvin</span>
        <span class="sub">psychology + EMDR</span>
      </div>
      <p class="tagline">
        <span class="sep"></span>Connect
        <span class="sep"></span>Integrate
        <span class="sep"></span>Evolve
      </p>
    </div>
  </section>
</body>
</html>
```